New business card for my lawn and landscape business

Hollin Yard and Building is a full-service lawn care, landscaping, and light construction company serving Paragould and the Northeast Arkansas region. The business is owned and operated by Dorian Waltham, with a reputation for hands-on, detail-oriented service, dependable crews, and quality results for both residential and commercial clients. A well regarded business with great reviews.
Owner Dorian Waltham
Hollinyardandbuilding.example

Target Market(s)

Commercial, Middle, and upper class in north east Arkansas

Industry/Entity Type

Lawn maintenance and landscape

Contact Information for Business Card

Hollin Yard And Building Professional lawn care, landscaping, and property improvement in Northeast Arkansas. • lawn maintenance •lawn treatments and weed control • exterior projects • Custom landscape design & installation • Sod, trees, rock & drainage solutions • Residential & commercial services Reliable. Detailed. Done right.

Requirements
Must have
• Business name, service area, list of some of our services, clean design that represents
Nice to have
• Unique. Different design element than just grass because its already in n the logo. Picture of a warm season (south) lawn or landscape. Pictures of the type of work we do

```html
<!DOCTYPE html>
<html lang="en">
<head>
<meta charset="utf-8">
<title>Hollin Yard and Building – Business Card</title>
<link href="https://fonts.googleapis.com/css2?family=Montserrat:wght@400;600;700&family=Oswald:wght@700&family=Merriweather:ital,wght@1,700&family=Roboto:wght@700&display=swap" rel="stylesheet">
<style>
  :root {
    --bg: #d4d4d4;
    --grass-dark: #3f8a1f;
    --grass-mid: #4c9c26;
    --grass-light: #5aad30;
    --brand-green: #5bb131;
    --headline-green: #7fd04a;
    --white: #ffffff;
    --shadow-grey: #b9b9bd;
    --ink-white: #f4f8f0;
  }
  * { margin: 0; padding: 0; box-sizing: border-box; }
  html, body { width: 1200px; height: 800px; overflow: hidden; }
  body {
    background: var(--bg);
    font-family: "Montserrat", Arial, sans-serif;
    position: relative;
  }
  .card {
    position: absolute;
    width: 620px;
    height: 354px;
    overflow: hidden;
    box-shadow: 0 10px 24px rgba(0,0,0,0.22);
  }
  .card--front { left: 70px; top: 34px; }
  .card--back { left: 510px; top: 412px; }

  .grass-fill {
    position: absolute; inset: 0;
    background: radial-gradient(ellipse at 40% 60%, var(--grass-light), var(--grass-mid) 55%, var(--grass-dark));
  }
  .front-shape { position: absolute; inset: 0; }

  .brand {
    position: absolute;
    left: 300px; top: 44px;
    display: flex; align-items: center; gap: 14px;
  }
  .brand__dot {
    width: 64px; height: 64px; border-radius: 50%;
    border: 6px solid var(--brand-green);
    flex: none;
  }
  .brand__name {
    color: var(--brand-green);
    font-weight: 700;
    font-size: 24px;
    line-height: 1.1;
    text-transform: uppercase;
    letter-spacing: 1px;
    width: 210px;
  }

  .contact {
    position: absolute;
    left: 34px; bottom: 22px;
    color: var(--ink-white);
  }
  .contact__name {
    font-weight: 700; font-size: 22px; letter-spacing: 1.5px;
    text-transform: uppercase;
  }
  .contact__role { font-size: 14px; margin-bottom: 10px; }
  .contact__list { list-style: none; font-size: 14px; line-height: 1.45; }
  .contact__list li { display: flex; align-items: center; gap: 8px; }
  .contact__list svg { width: 14px; height: 14px; flex: none; }
  .contact__address { margin-top: 8px; padding-left: 22px; font-size: 14px; line-height: 1.35; }

  .back-content {
    position: absolute; inset: 0;
    padding: 34px 30px 0;
    text-align: center;
  }
  .back__headline {
    font-family: "Oswald", "Arial Narrow", sans-serif;
    font-weight: 700;
    font-size: 40px;
    color: var(--headline-green);
    text-transform: uppercase;
    letter-spacing: 0.5px;
    line-height: 1.1;
  }
  .back__tagline {
    font-family: "Merriweather", Georgia, serif;
    font-style: italic; font-weight: 700;
    color: var(--ink-white);
    font-size: 17px;
    line-height: 1.45;
    margin-top: 14px;
  }
  .services {
    position: absolute;
    left: 30px; right: 24px; bottom: 32px;
    display: flex; justify-content: space-between;
    font-family: "Roboto", Arial, sans-serif;
    font-weight: 700;
    color: var(--ink-white);
    font-size: 14px;
  }
  .services ul { list-style: none; line-height: 1.6; }
  .services li { display: flex; align-items: center; gap: 7px; }
  .services svg { width: 13px; height: 13px; flex: none; }
  .services__col--right { align-self: flex-start; margin-top: -26px; }
</style>
</head>
<body>

<section class="card card--front" aria-label="Business card front">
  <div class="grass-fill" role="img" aria-label="Warm-season lawn grass texture"></div>
  <svg class="front-shape" viewBox="0 0 620 354" preserveAspectRatio="none" aria-hidden="true">
    <ellipse cx="400" cy="0" rx="420" ry="164" fill="var(--shadow-grey)"/>
    <ellipse cx="420" cy="-6" rx="400" ry="160" fill="var(--white)"/>
  </svg>

  <div class="brand">
    <span class="brand__dot"></span>
    <span class="brand__name">Hollin Yard and Building</span>
  </div>

  <div class="contact">
    <p class="contact__name">Dorian Waltham</p>
    <p class="contact__role">Owner</p>
    <ul class="contact__list">
      <li>
        <svg viewBox="0 0 16 16"><path d="M4 1.5 6.2 4 5 5.6c.8 1.9 2.3 3.4 4.2 4.3L10.8 8.7l2.6 2.2-1 2.6C7 13.2 2.8 9 2.4 3.4z" fill="none" stroke="currentColor" stroke-width="1.4"/></svg>
        044-555 010 246
      </li>
      <li>
        <svg viewBox="0 0 16 16"><rect x="1.5" y="3.5" width="13" height="9" fill="none" stroke="currentColor" stroke-width="1.4"/><path d="M1.5 3.5 8 9l6.5-5.5" fill="none" stroke="currentColor" stroke-width="1.4"/></svg>
        hello@hollinyard.example
      </li>
      <li>
        <svg viewBox="0 0 16 16"><circle cx="8" cy="8" r="6.3" fill="none" stroke="currentColor" stroke-width="1.4"/><path d="M1.7 8h12.6M8 1.7c-3 3.4-3 9.2 0 12.6M8 1.7c3 3.4 3 9.2 0 12.6" fill="none" stroke="currentColor" stroke-width="1.2"/></svg>
        www.hollinyardandbuilding.example
      </li>
    </ul>
    <p class="contact__address">88 Orchard Row, Paragould<br>72450, United States</p>
  </div>
</section>

<section class="card card--back" aria-label="Business card back">
  <div class="grass-fill" role="img" aria-label="Warm-season lawn grass texture"></div>
  <div class="back-content">
    <h1 class="back__headline">Hollin Yard and Building</h1>
    <p class="back__tagline">Professional lawn care, landscaping and property<br>improvement in Northeast Arkansas.</p>
  </div>
  <div class="services">
    <ul class="services__col">
      <li><svg viewBox="0 0 14 14"><circle cx="7" cy="7" r="5.8" fill="none" stroke="currentColor" stroke-width="1.3"/><circle cx="7" cy="7" r="2.2" fill="currentColor"/></svg>Lawn maintenance</li>
      <li><svg viewBox="0 0 14 14"><circle cx="7" cy="7" r="5.8" fill="none" stroke="currentColor" stroke-width="1.3"/><circle cx="7" cy="7" r="2.2" fill="currentColor"/></svg>Lawn treatments and weed control</li>
      <li><svg viewBox="0 0 14 14"><circle cx="7" cy="7" r="5.8" fill="none" stroke="currentColor" stroke-width="1.3"/><circle cx="7" cy="7" r="2.2" fill="currentColor"/></svg>Exterior projects</li>
    </ul>
    <ul class="services__col services__col--right">
      <li><svg viewBox="0 0 14 14"><circle cx="7" cy="7" r="5.8" fill="none" stroke="currentColor" stroke-width="1.3"/><circle cx="7" cy="7" r="2.2" fill="currentColor"/></svg>Custom landscape design &amp; installation</li>
      <li><svg viewBox="0 0 14 14"><circle cx="7" cy="7" r="5.8" fill="none" stroke="currentColor" stroke-width="1.3"/><circle cx="7" cy="7" r="2.2" fill="currentColor"/></svg>Sod, trees, rock &amp; drainage solutions</li>
      <li><svg viewBox="0 0 14 14"><circle cx="7" cy="7" r="5.8" fill="none" stroke="currentColor" stroke-width="1.3"/><circle cx="7" cy="7" r="2.2" fill="currentColor"/></svg>Residential &amp; commercial services</li>
    </ul>
  </div>
</section>

</body>
</html>
```